WHAT COMES NEXT? Discovering the reason for being beside the Inner Lamp

Creating a book that is about living a spiritual life. The book is about letting go of the materialistic world and finding happiness through self realisation and enlightenment. The contents page is below that gives an idea of what is contained in the book.

The book is based on the writings of the Sikhs - from India. But it is written in a universal way that is understandable to all.

CONTENTS
Living for a purpose
- Born to be original! Dying as a copy!
- My relationship with everything but me!
- What is my purpose?

Life as a human being!
- Stages of Life
- Five Weaknesses

What is driving our lives?
- Information overload?
- What are your drivers?
- Giving life meaning

You reap what you sow
- Is my destiny written?
- Good and bad actions
- Maya – the illusion and it’s three modes

Slow down and let go
- The mind in overdrive
- Being aware of our mental health
- Why Slow Down?

The Guidance of the Guru
- Why do I need a Guru?
- What the Guru gives you
- Gurbani – the Guru’s Words

Staying connected
- Repeating the Mantra
- Doing two things at once
- Remembering in times of difficulty

Cultivating virtues
- Theory vs Practice
- Virtues and true religion
- Some key virtues

The Mystical Creation
- Experiencing ecstasy
- Enlightenment and intuition
- Spiritual Transformation

Good Company
- How do my companions affect me?
- The company of Saintly people
- Obtaining the fruits that the Guru describes

Serving selflessly
- Serving is our purpose
- Being grateful
- Being generous

Ten things to change your life today

Target Market(s)

All those who want to learn about spirituality. We are targeting young and middle aged but not necessarily ruling out older demographic.

Requirements
Must have
• The book cover:

- exciting and intriguing
- theme is "why am I here" in this world
- some kind of lean towards enlightenment
Nice to have
• It is not essential but the cover could subtly show something about the Sikh faith. Can discuss this further if necessary.
Should not have
• Should not:

- look dull and boring
- don't want it to look like a Buddhism book

```html
<!DOCTYPE html>
<html lang="en">
<head>
<meta charset="UTF-8">
<title>What Comes Next – Book Cover</title>
<link rel="stylesheet" href="https://fonts.googleapis.com/css2?family=Cinzel:wght@400;700;900&display=swap">
<style>
  :root {
    --ink: #0c0a0b;
    --panel: #d8c483;
    --light: #f4efe6;
    --shade: rgba(8, 6, 10, 0.72);
    --art-deep: #120b16;
    --art-violet: #3b1d4a;
    --art-plum: #5a2a55;
    --art-amber: #8a6a2c;
  }
  * { margin: 0; padding: 0; box-sizing: border-box; }
  html, body { width: 768px; height: 1200px; overflow: hidden; background: var(--ink); }
  .cover {
    position: relative;
    width: 768px;
    height: 1200px;
    overflow: hidden;
    font-family: "Cinzel", serif;
    background: var(--art-deep);
  }
  .cover-art {
    position: absolute;
    left: 0;
    width: 768px;
  }
  .cover-art--top {
    top: 0;
    height: 315px;
    background:
      radial-gradient(ellipse at 80% 30%, var(--art-plum) 0%, transparent 55%),
      radial-gradient(ellipse at 15% 70%, var(--art-violet) 0%, transparent 60%),
      linear-gradient(160deg, #1a0f1f 0%, var(--art-deep) 60%, #0a070c 100%);
  }
  .cover-art--bottom {
    top: 870px;
    height: 330px;
    background:
      radial-gradient(ellipse at 48% 30%, var(--art-amber) 0%, transparent 40%),
      radial-gradient(ellipse at 20% 50%, var(--art-plum) 0%, transparent 55%),
      radial-gradient(ellipse at 85% 40%, var(--art-violet) 0%, transparent 50%),
      linear-gradient(180deg, #1a0f1f 0%, var(--art-deep) 100%);
  }
  .bestseller {
    position: absolute;
    top: 96px;
    width: 100%;
    text-align: center;
    font-size: 14px;
    letter-spacing: 1.5px;
    color: var(--light);
  }
  .subtitle-band {
    position: absolute;
    top: 180px;
    left: 0;
    width: 100%;
    height: 118px;
    background: var(--shade);
  }
  .subtitle {
    position: absolute;
    top: 130px;
    width: 100%;
    text-align: center;
    font-size: 40px;
    font-weight: 400;
    font-variant: small-caps;
    line-height: 58px;
    letter-spacing: 2px;
    color: var(--light);
  }
  .title-panel {
    position: absolute;
    top: 315px;
    left: 0;
    width: 768px;
    height: 555px;
    background: var(--panel);
  }
  .title {
    position: absolute;
    top: 118px;
    left: 70px;
    right: 40px;
    text-align: center;
    font-size: 82px;
    font-weight: 700;
    line-height: 120px;
    color: var(--ink);
  }
  .spine-credit {
    position: absolute;
    left: 26px;
    top: 45px;
    writing-mode: vertical-rl;
    font-size: 9px;
    letter-spacing: 1.5px;
    color: #4a3f25;
    white-space: nowrap;
  }
  .author-band {
    position: absolute;
    top: 1050px;
    left: 0;
    width: 100%;
    height: 90px;
    background: var(--shade);
  }
  .author {
    position: absolute;
    top: 1050px;
    width: 100%;
    text-align: center;
    font-size: 72px;
    font-weight: 700;
    line-height: 90px;
    color: var(--light);
  }
</style>
</head>
<body>
  <main class="cover">
    <div class="cover-art cover-art--top" role="img" aria-label="Abstract dark violet and magenta light streaks"></div>
    <div class="cover-art cover-art--bottom" role="img" aria-label="Abstract glowing shards of amber, green and violet light"></div>

    <p class="bestseller">THE MERIDIAN POST BESTSELLER</p>
    <div class="subtitle-band"></div>
    <h2 class="subtitle">Discovering the reason<br>for being beside<br>the Inner Lamp</h2>

    <section class="title-panel">
      <p class="spine-credit">OWEN HALE / LANTERNS AND ECHOES / QUILLSTONE PRESS</p>
      <h1 class="title">WHAT COMES<br>NEXT?</h1>
    </section>

    <div class="author-band"></div>
    <p class="author">Inner Lamp</p>
  </main>
</body>
</html>
```